Quorvella Website Redesign

We need a redesign of the company website.

We're a company, based in the UK, called Quorvella. We develop software for the Healthcare Industry, used by medical professionals throughout the UK on a daily basis.

We have a suite of tools that form the Quorvella Platform, and all are web-based.

We want to communicate that our software is not only innovative but is the best available, easy to use, and provides exceptional quality and RoI.

Additionally, we want our existing customers to be able to see what else we can offer them.

A site map is attached.
Updates

Hi Everyone,

As we approach the deadline for submissions, we’ve shortlisted threedesigns that we felt were the best of the submissions and have asked thedesigners to make some additional changes and produce some content pages so wecan see what’s beneath the Home page in the rest of the site.

Thank you all for your submissions – there was an awful lot ofdisagreement among everyone here over which designs we thought were best andsome of those that haven’t made it into the final three were very well liked.

Those in the final three have been messaged individually and have theirdesigns as the only non-eliminated ones showing. We would ask at this stagethat anyone not in the final three please do no further work or submitadditional designs as we are approaching the deadline and will not be able toprovide sufficient feedback to allow any changes in a short space of time.

Kind regards,
The Quorvella Team

Target Market(s)

Nurses and medical professionals in western-speaking countries, most notably in the UK.

Predominantly, we expect it will be senior medical staff that will be viewing (and using) our website - some will be existing customers and some will be new or potential customers.

Industry/Entity Type

Medical

Requirements
Must have
• Area to showcase and provide information about products.
• Company information - who we are and why you should choose us.
• News and events - blog, archive newsletters, publications, etc.
• Support section for existing customers - FAQ, Forum, Manuals.
• Contact page.
• We also feel that we'd like to have our telephone number and primary email address visible at all times, with an immediate ability for users to request a demonstration.
Nice to have
• A "My Quorvella" area would be nice at some point, though that's something for further down the line.

```html
<!DOCTYPE html>
<html lang="en">
<head>
<meta charset="utf-8">
<title>QuorvellaHealth – Contact</title>
<link href="https://fonts.googleapis.com/css2?family=Arimo:wght@400;700&family=Inter:wght@400;600;700&family=Noto+Sans:wght@400&family=Roboto+Condensed:wght@400&display=swap" rel="stylesheet">
<style>
:root{
  --blue:#1a86e0;
  --blue-dark:#0b5ea8;
  --blue-light:#45aef0;
  --grey-band:#7b7c80;
  --text:#555;
  --text-dark:#333;
  --field:#ececec;
  --field-border:#9a9a9a;
  --green:#7ec42a;
  --green-dark:#5ea414;
  --tick:#2fae1c;
  --link:#1a86e0;
  --white:#fff;
  --yellow:#ffe100;
}
*{box-sizing:border-box;margin:0;padding:0}
html,body{width:945px;height:1200px;overflow:hidden;background:var(--white)}
body{position:relative;font-family:"Arimo",Arial,sans-serif;color:var(--text)}
.abs{position:absolute}

/* header */
.brand{left:121px;top:14px}
.brand-name{font-family:"Arimo",sans-serif;font-weight:700;font-size:21px;color:var(--blue);letter-spacing:-.2px}
.brand-tag{font-family:"Arimo",sans-serif;font-size:8px;color:#777;letter-spacing:.9px;margin-top:2px;border-top:1px solid #ccc;padding-top:2px}
.header-contact{left:450px;top:31px;font-family:"Roboto Condensed",sans-serif;font-size:16.5px;color:#777;white-space:nowrap}
.header-contact b{font-weight:400;color:var(--blue);margin-right:4px}
.header-contact span{margin-right:12px}

.nav{left:0;top:76px;width:945px;height:19px;font-size:10px;color:#444}
.nav a{position:absolute;top:3px;color:#444;text-decoration:none;white-space:nowrap}
.nav .sep{position:absolute;top:3px;color:#444}
.nav .tab{position:absolute;left:630px;top:-3px}
.nav a.active{color:var(--white)}
.band{left:0;top:95px;width:945px;height:23px;background:var(--grey-band)}

/* hero */
.hero{left:0;top:118px;width:945px;height:195px;background:linear-gradient(180deg,#1a87db 0%,#2a9ae6 50%,#3ba8ee 100%)}
.hero-title{left:120px;top:165px;font-family:"Arimo",sans-serif;font-weight:700;font-size:20.5px;line-height:25px;color:var(--white);letter-spacing:-1.3px;white-space:nowrap}
.hero-text{left:120px;top:228px;font-family:"Noto Sans",sans-serif;font-size:9.8px;line-height:17px;color:var(--white);white-space:nowrap}
.hero-photo{left:490px;top:120px;width:316px;height:193px;background:radial-gradient(ellipse at 55% 60%,#f4f7fa 0%,#dfe8ef 40%,rgba(60,170,240,0) 72%)}

/* main */
.page-title{left:129px;top:335px;font-family:"Inter",sans-serif;font-weight:700;font-size:16px;color:var(--text-dark);letter-spacing:-.8px}
.staff-photo{left:128px;top:372px;width:125px;height:83px;border:1px solid #9aa7b3;background:linear-gradient(135deg,#c8d6e2,#eef2f5 55%,#aebfcd)}
.intro-title{left:273px;top:377px;font-family:"Arimo",sans-serif;font-weight:700;font-size:13px;color:#666;white-space:nowrap}
.intro-text{left:277px;top:400px;font-size:8.2px;line-height:17px;color:#666;letter-spacing:-.2px;white-space:nowrap}

.address{font-family:"Noto Sans",sans-serif;font-size:8.6px;line-height:16.8px;color:#444;font-style:normal;white-space:nowrap}
.addr-uk{left:129px;top:478px}
.addr-ie{left:409px;top:478px}
.addr-cy{left:406px;top:524px}
.addr-divider{left:356px;top:483px;height:80px;border-left:1px dotted #777}

.form-card{left:125px;top:587px;width:458px;height:401px;border:1px solid #cfcfcf;border-radius:12px}
.label{font-size:8px;color:#666;white-space:nowrap}
.field{height:18px;width:156px;background:var(--field);border:1px solid var(--field-border);border-radius:9px;box-shadow:inset 0 2px 2px rgba(0,0,0,.12)}
.select{font-size:8.5px;font-style:italic;color:#555;padding:3px 0 0 16px}
.select::after{content:"▾";position:absolute;right:5px;top:2px;font-style:normal;font-size:9px;color:#333}
.notes{left:204px;top:698px;width:292px;height:178px;background:var(--field);border:1px solid var(--field-border);border-radius:12px;box-shadow:inset 0 2px 3px rgba(0,0,0,.1)}
.word-count{left:507px;top:864px;font-size:8px;font-style:italic;color:#7a1a6a}
.code-box{left:257px;top:900px;width:58px;height:19px;border:1px solid #557;background:repeating-linear-gradient(45deg,#b8c6e8 0 2px,#e4eaf7 2px 4px)}
.code-field{left:328px;top:899px;width:62px;height:21px}

.btn{height:24px;border-radius:6px;background:linear-gradient(180deg,#5fb1f5 0%,#2e8fe8 50%,#1a72cf 100%);color:var(--white);font-size:8.5px;text-align:center;line-height:24px;box-shadow:0 2px 2px rgba(0,0,0,.3);letter-spacing:-.3px}

.col-divider{left:611px;top:342px;height:597px;border-left:1px dotted #777}

/* sidebar */
.demo-btn{left:634px;top:339px;width:181px;height:38px;border-radius:5px;background:linear-gradient(180deg,#9ad74a 0%,var(--green) 55%,var(--green-dark) 100%);color:var(--white);font-family:"Inter",sans-serif;font-weight:700;font-size:11.5px;letter-spacing:-.6px;line-height:38px;padding-left:20px;white-space:nowrap}
.demo-btn span{color:#cdeea8;margin-right:6px;font-size:9px}
.side-title{font-family:"Inter",sans-serif;font-weight:700;font-size:15.5px;color:var(--text-dark);letter-spacing:-.9px;white-space:nowrap}
.why-list{left:652px;top:444px;list-style:none}
.why-list li{height:21px;display:flex;align-items:center;font-size:8.2px;color:#555;letter-spacing:-.2px;white-space:nowrap}
.why-list svg{margin-right:10px}
.side-label{font-size:8.2px;color:#555}
.side-field{width:118px;height:18px;background:var(--white);border:1px solid #aaa;border-radius:9px;box-shadow:inset 0 2px 2px rgba(0,0,0,.12)}
.help{left:657px;top:677px;width:20px;height:17px;border:1px solid #999;border-radius:4px;font-size:8px;text-align:center;line-height:15px;color:#333}
.side-note{font-size:8.2px;color:#555;letter-spacing:-.2px;white-space:nowrap}
.side-note a{color:var(--link);text-decoration:none}

/* footer */
.footer{left:0;top:1010px;width:945px;height:136px;background:linear-gradient(180deg,#1788d7 0%,#1273c0 60%,#0e62ab 100%)}
.copyright-bar{left:0;top:1146px;width:945px;height:54px;background:linear-gradient(180deg,#1582d1,#0b5ba3)}
.copyright{left:0;top:1160px;width:945px;text-align:center;font-size:8.2px;color:var(--white);letter-spacing:-.2px}
.copyright a{color:var(--yellow);text-decoration:none}
.foot-title{font-family:"Inter",sans-serif;font-weight:700;font-size:15.5px;color:var(--white);letter-spacing:-.9px;white-space:nowrap}
.foot-text{font-size:8.2px;color:var(--white);line-height:21px;letter-spacing:-.2px;white-space:nowrap}
.social{width:14px;height:14px;border-radius:3px;background:#d8ecfa}
.news-img{left:652px;top:1062px;width:32px;height:20px;background:linear-gradient(135deg,#f2f2f2,#bfc4c8);transform:rotate(-12deg);border-radius:2px}
.news-field{left:654px;top:1097px;width:103px;height:19px;background:#c9cfd5;border:1px solid #8fa0b0;border-radius:9px;box-shadow:inset 0 2px 2px rgba(0,0,0,.2)}
.go-btn{left:769px;top:1095px;width:33px;height:17px;line-height:17px;font-size:8.5px}
</style>
</head>
<body>

<header>
  <div class="abs brand">
    <div class="brand-name">QuorvellaHealth</div>
    <div class="brand-tag">Bringing Technology to Healthcare</div>
  </div>
  <div class="abs header-contact"><b>Email</b><span>hello@quorvellahealth.example</span><b>Call</b>+44 (0) 20 7946 0321</div>

  <nav class="abs nav">
    <svg class="tab" width="104" height="22" viewBox="0 0 104 22"><path d="M0 22 C6 22 6 0 16 0 H88 C98 0 98 22 104 22 Z" fill="#7b7c80"/></svg>
    <a style="left:142px">Home</a>
    <span class="sep" style="left:201px">|</span>
    <a style="left:211px">Products &amp; Services</a>
    <span class="sep" style="left:305px">|</span>
    <a style="left:324px">About&nbsp; Quorvella</a>
    <span class="sep" style="left:411px">|</span>
    <a style="left:432px">News &amp; Events</a>
    <span class="sep" style="left:518px">|</span>
    <a style="left:556px">Support</a>
    <span class="sep" style="left:629px">|</span>
    <a class="active" style="left:667px">Contact</a>
    <span class="sep" style="left:736px">|</span>
    <a style="left:760px">My Quorvella</a>
  </nav>
  <div class="abs band"></div>
</header>

<section class="abs hero"></section>
<div class="abs hero-photo" role="img" aria-label="Photo of four smiling medical staff in white coats and scrubs"></div>
<h1 class="abs hero-title">Lorem ipsum dolor sit amet, consecte-<br>tur adipiscing Content. Am ipsum dolor</h1>
<p class="abs hero-text">Lorem ipsum dolor sit amet, consectetur adipiscing elit. Pellen-<br>tesque non ligula id eros consequat porttitor et in erat. Ali</p>

<main>
  <h2 class="abs page-title">Contact</h2>
  <div class="abs staff-photo" role="img" aria-label="Photo of a doctor holding a clipboard in a bright office"></div>
  <h3 class="abs intro-title">Lorem ipsum dolor sit amet, consectetur</h3>
  <p class="abs intro-text">imperdiet enim lobortis volutpat in nec arcu. Nunc facilisis, orci a euismod<br>ornare, justo dui sagittis purus, accumsan aliquam mauris nulla eu ipsum.<br>Fusce lacus velit, pellentesque quis egestas in, tincidunt nec leo.</p>

  <address class="abs address addr-uk">Quorvella<br>48 Aldwyn Crescent, London N7 2QX<br>United Kingdom<br>Tel.: +44 (0) 20 7946 0321<br>Fax: +44 (0) 20 7946 0458</address>
  <div class="abs addr-divider"></div>
  <address class="abs address addr-ie">Republic Of Ireland<br>Tel.: +353 (0) 1 555 0187</address>
  <address class="abs address addr-cy">Greece and Cyprus<br>Tel.: +357 22 555 014</address>

  <form class="abs form-card"></form>
  <span class="abs label" style="left:160px;top:616px">Name :</span>
  <div class="abs field" style="left:204px;top:614px"></div>
  <span class="abs label" style="left:160px;top:644px">Email :</span>
  <div class="abs field" style="left:204px;top:640px"></div>
  <span class="abs label" style="left:160px;top:672px">Subject :</span>
  <div class="abs field select" style="left:204px;top:667px">Choose Here</div>
  <span class="abs label" style="left:160px;top:700px">Notes:</span>
  <div class="abs notes"></div>
  <span class="abs word-count">2000 words</span>
  <span class="abs label" style="left:160px;top:906px">Please enter the code :</span>
  <div class="abs code-box" role="img" aria-label="Security code image"></div>
  <div class="abs field code-field"></div>
  <div class="abs btn" style="left:411px;top:935px;width:45px">Submit</div>
  <div class="abs btn" style="left:460px;top:935px;width:45px">Reset</div>

  <div class="abs col-divider"></div>
</main>

<aside>
  <div class="abs demo-btn"><span>▶▶</span>Request A Demo Here!</div>

  <h2 class="abs side-title" style="left:652px;top:407px">Why use Us</h2>
  <ul class="abs why-list">
    <li><svg width="14" height="18" viewBox="0 0 14 18"><path d="M1 10 L5 16 L13 1" fill="none" stroke="#2fae1c" stroke-width="2.5" stroke-linecap="round"/></svg>Vestibulum laoreet eros</li>
    <li><svg width="14" height="18" viewBox="0 0 14 18"><path d="M1 10 L5 16 L13 1" fill="none" stroke="#2fae1c" stroke-width="2.5" stroke-linecap="round"/></svg>Suspendisse vulputate com</li>
    <li><svg width="14" height="18" viewBox="0 0 14 18"><path d="M1 10 L5 16 L13 1" fill="none" stroke="#2fae1c" stroke-width="2.5" stroke-linecap="round"/></svg>Nunc adipiscing tellus non nisl</li>
    <li><svg width="14" height="18" viewBox="0 0 14 18"><path d="M1 10 L5 16 L13 1" fill="none" stroke="#2fae1c" stroke-width="2.5" stroke-linecap="round"/></svg>Vivamus vestibulum leo ut orc</li>
    <li><svg width="14" height="18" viewBox="0 0 14 18"><path d="M1 10 L5 16 L13 1" fill="none" stroke="#2fae1c" stroke-width="2.5" stroke-linecap="round"/></svg>Vivamus placerat diam at a</li>
  </ul>

  <h2 class="abs side-title" style="left:652px;top:562px">My Quorvella Area</h2>
  <span class="abs side-label" style="left:656px;top:596px">Name</span>
  <div class="abs side-field" style="left:670px;top:608px"></div>
  <span class="abs side-label" style="left:656px;top:635px">Pasword</span>
  <div class="abs side-field" style="left:670px;top:651px"></div>
  <div class="abs help">?</div>
  <p class="abs side-note" style="left:685px;top:681px">Not a member? <a>Sign Up&nbsp; now!</a></p>
  <p class="abs side-note" style="left:685px;top:699px">Forgot Password? <a>Contact Us!</a></p>
  <div class="abs btn" style="left:690px;top:724px;width:45px">Submit</div>
  <div class="abs btn" style="left:740px;top:724px;width:45px">Reset</div>
</aside>

<footer>
  <div class="abs footer"></div>
  <h2 class="abs foot-title" style="left:131px;top:1031px">Contact Us</h2>
  <p class="abs foot-text" style="left:132px;top:1059px">Quorvella Ltd,<br>48 Aldwyn Crescent,<br>London N7 2QX United Kingdom .</p>
  <p class="abs foot-text" style="left:289px;top:1059px">Tel.: +44 (0) 20 7946 0321<br>Fax: +44 (0) 20 7946 0458</p>

  <h2 class="abs foot-title" style="left:444px;top:1029px">Get Involved</h2>
  <div class="abs social" style="left:452px;top:1056px"></div>
  <div class="abs social" style="left:452px;top:1077px"></div>
  <div class="abs social" style="left:452px;top:1098px"></div>
  <p class="abs foot-text" style="left:483px;top:1054px">We Tweet you Follow<br>Put Your Face in our Book<br>Connect my proffesional line</p>

  <h2 class="abs foot-title" style="left:644px;top:1031px">Newsletter</h2>
  <div class="abs news-img" role="img" aria-label="Folded newspaper"></div>
  <p class="abs foot-text" style="left:693px;top:1066px">Sign Up for our News leteer</p>
  <div class="abs news-field"></div>
  <div class="abs btn go-btn">GO</div>

  <div class="abs copyright-bar"></div>
  <p class="abs copyright">Copyright © 2008 Quorvella - All rights reserved. Please see [ <a>Website Terms &amp; Conditions</a>] for details .</p>
</footer>

</body>
</html>
```